3 Backs for Universal Flyer Front

We have a One-sided postcard sized flyer and would like to create a series of backs to use for it.
The front side of the flyer will remain generic, the brown Marrowgate Hollow image, with the 3 backs all incorporating the Marrowgate Hollow branding. The 3 different backs are:
1. Dusk Among the Barrels event. This is a green leaf design, with date and contact details
2. Coupon voucher. The ability to use in showbags/promo events as a coupon voucher to encourage customers to shop again. The ability to change the voucher code and the voucher amount.
3. Gift voucher. Basic details of To: From: and Amount

We would like to use these backs for the next few years so no year dates should be included.I have attached a previous flyer that we used for our Dusk Among the Barrels event. We like the green leafy detail. This would not be included on the 2nd and 3rd design requests. I have included the image of the generic cover. Even if we could incorporate some of the rose/vines/bird artwork into the coupon voucher and gift voucher. All 3 would ideally have a neutral background with text that is easy to see against.

Target Market(s)

Wine Consumers

Colors

Designer to choose colors to be used in the design.

Requirements
Must have
• Dusk Among the Barrels back should have the dusk among the barrels logo (years removed) and the green vine work.
• The other 2 (coupon and gift voucher) should be reasonably similar in design.
• They need minimum info on each.
• 1. Dusk Among the Barrels: 2nd Saturday of November. 417 Tessaly Lane, Coombridge Flats WA, Phone 08 9730 6281 or email info@marrowgatehollow.example.com.au to book
• 2. Voucher coupon:
• Buy 6 bottles or more at our online store of Cellardoor to receive $XX off.
• 1 voucher per customer
• 3. Gift Voucher:
• Needs fields such as TO: FROM: Amount: Valid from: Valid for 12 months. Not redeemable for cash
Nice to have
• Coupon and gift voucher nice to tie in with cover with bird/vine/rose artwork. Keep on neutral colour back so text is easy to see.
Should not have
• All designs must be able to be used for the next few years so no dates

```html
<!DOCTYPE html>
<html lang="en">
<head>
<meta charset="utf-8">
<title>Marrowgate Hollow – Coupon Voucher</title>
<link rel="stylesheet" href="https://fonts.googleapis.com/css2?family=Pinyon+Script&family=Tenor+Sans&family=Tinos&family=Open+Sans&display=swap">
<style>
  :root {
    --card: #ffffff;
    --ornament: #dcdbd3;
    --ornament-soft: rgba(220, 219, 211, 0);
    --script: #8f8d82;
    --taupe: #8a897c;
    --figure: #646566;
    --brand: #4b3f3a;
    --body: #666666;
    --rule: #9a9a9a;
  }
  * { margin: 0; padding: 0; box-sizing: border-box; }
  html, body { width: 1200px; height: 874px; overflow: hidden; background: var(--card); }
  .voucher { position: relative; width: 1200px; height: 874px; background: var(--card); overflow: hidden; }

  .ornament { position: absolute; }
  .ornament--vines-top { left: 0; top: 0; width: 830px; height: 160px;
    background: linear-gradient(180deg, var(--ornament) 0%, var(--ornament-soft) 100%); opacity: .55; }
  .ornament--vines-left { left: 0; top: 0; width: 210px; height: 590px;
    background: linear-gradient(90deg, var(--ornament) 0%, var(--ornament-soft) 100%); opacity: .7; }
  .ornament--rose { right: 0; bottom: 0; width: 390px; height: 335px;
    background: radial-gradient(ellipse at 60% 60%, var(--ornament) 0%, var(--ornament-soft) 72%); opacity: .8; }

  .brand { position: absolute; left: 990px; top: 82px; width: 180px; text-align: center;
    font-family: "Tenor Sans", sans-serif; color: var(--brand); letter-spacing: 1px; line-height: 1.2; }
  .brand__mark { display: block; width: 22px; height: 22px; margin: 0 auto 6px; border-radius: 50%; background: var(--brand); }
  .brand__name { font-size: 22px; }

  .title { position: absolute; left: 0; width: 1216px; top: 108px; text-align: center;
    font-family: "Pinyon Script", cursive; font-size: 92px; color: var(--script); }

  .offer-terms { position: absolute; left: 0; width: 1216px; top: 233px; text-align: center;
    font-family: "Tenor Sans", sans-serif; font-size: 30px; line-height: 43px; color: var(--taupe); }
  .offer-terms .qty { font-size: 40px; }

  .amount { position: absolute; font-family: "Tinos", serif; }
  .amount__currency { left: 422px; top: 345px; font-size: 112px; color: var(--taupe); }
  .amount__value { left: 490px; top: 376px; font-size: 196px; line-height: 1; color: var(--figure); letter-spacing: -4px; }
  .amount__label { left: 720px; top: 466px; font-size: 62px; line-height: 1; color: var(--taupe); }

  .promo-code { position: absolute; left: 504px; top: 578px; width: 254px; height: 41px;
    border: 2px solid var(--rule); font-family: "Open Sans", sans-serif; font-size: 19px;
    color: #444; text-align: center; line-height: 37px; background: var(--card); }

  .footnote { position: absolute; left: 55px; top: 800px; font-family: "Open Sans", sans-serif;
    font-size: 19px; color: var(--body); }
  .website { position: absolute; right: 61px; top: 799px; font-family: "Tinos", serif;
    font-size: 20px; color: #3f3f3f; }
</style>
</head>
<body>
<main class="voucher">
  <div class="ornament ornament--vines-top" role="img" aria-label="Engraved rose vine with leaves and thorns along the top edge"></div>
  <div class="ornament ornament--vines-left" role="img" aria-label="Engraved rose stems and buds climbing the left edge"></div>
  <div class="ornament ornament--rose" role="img" aria-label="Large engraved rose with leaves in the lower right corner"></div>

  <div class="brand">
    <span class="brand__mark"></span>
    <div class="brand__name">MARROWGATE<br>HOLLOW</div>
  </div>

  <h1 class="title">Coupon Voucher</h1>

  <p class="offer-terms">Buy <span class="qty">6</span> bottles or more at our online store or<br>Cellar Door to receive</p>

  <div class="amount amount__currency">$</div>
  <div class="amount amount__value">00</div>
  <div class="amount amount__label">OFF</div>

  <div class="promo-code">PROMO CODE : XXXXXXXX</div>

  <p class="footnote">* Limited to 1 (one) redemption per voucher and per customer only.</p>
  <p class="website">www.marrowgatehollow.example.com.au</p>
</main>
</body>
</html>
```